5 x 7 card advertising ash spreading

I need a new design for a double sided 5 x 7 horizontal post card to give to funeral homes so they can give them out to people who are interested in an ash spreading boat charter at sea for their loved one who has died. I want a simple, professional, classy, thoughtful design that I can include a summary of what we offer, what's included, our logo and and contact info. Even though we will include the "what" we offer, this piece needs to speak to the readers "why". I've included an AI excerpt about why people desire this as opposed to being buried.
What we offer: Attended service, Unattended service, Memorial service, Anniversary service. What's included: Certificate of Ash Spreading, Onboard refreshments, Personalized music. Our contact information: Tidewell Charters, www.tidewellcharters.example, 452 Marlowe St., Clearwater, FL 33755, (727) 555-0148

Target Market(s)

People visiting a funeral home planning their own or a relatives final wishes for ash spreading at sea

Industry/Entity Type

Private boat charters

Requirements
Must have
• Professional look, speaks to they "why", as well as includes the "what" we do.

```html
<!DOCTYPE html>
<html lang="en">
<head>
<meta charset="utf-8">
<title>Tidewell Charters – Ash Scattering Postcard</title>
<link href="https://fonts.googleapis.com/css2?family=Montserrat:wght@400;500;600;700;800&display=swap" rel="stylesheet">
<style>
  :root{
    --navy:#163a6e;
    --navy-deep:#10305f;
    --navy-panel:#21497f;
    --sky:#1592d3;
    --sky-light:#3aa7e0;
    --orange:#ef7421;
    --white:#ffffff;
    --stage:#dcdcde;
    --stamp:#b9babd;
    --sea:#5d9f90;
    --sea-light:#b9d3cc;
  }
  *{box-sizing:border-box;margin:0;padding:0}
  html,body{width:1091px;height:1200px;overflow:hidden}
  body{background:var(--stage);font-family:"Montserrat",Arial,sans-serif;position:relative}
  .card{position:absolute;left:164px;width:763px;height:545px;background:var(--white);overflow:hidden;box-shadow:0 6px 18px rgba(0,0,0,.18)}
  .card--front{top:30px}
  .card--back{top:625px}
  .card__art{position:absolute;inset:0}

  /* front */
  .brand{position:absolute;display:flex;align-items:center;gap:10px;font-weight:800;white-space:nowrap}
  .brand__dot{width:22px;height:22px;border-radius:50%;background:var(--orange);flex:none}
  .brand--front{left:44px;top:70px;font-size:30px;color:var(--white)}
  .headline{position:absolute;left:50px;top:262px;font-weight:800;font-size:66px;line-height:64px;letter-spacing:-1px;color:var(--navy)}
  .headline__accent{color:var(--sky)}
  .headline__sub{display:block;font-size:22px;line-height:28px;letter-spacing:0;font-weight:700;color:var(--navy);margin-top:10px}
  .tile{position:absolute;top:385px;height:135px;border:4px solid var(--white);border-radius:16px}
  .tile--shells{left:419px;width:157px;background:linear-gradient(135deg,#e8d6bf,#c9a27d 60%,#a9a49a)}
  .tile--dolphins{left:582px;width:159px;background:linear-gradient(160deg,#3f8c78,#7fb7a6 55%,#2f6d5c)}

  /* back */
  .brand--back{left:430px;top:62px;font-size:19px;color:var(--navy)}
  .stamp{position:absolute;left:646px;top:26px;width:89px;height:89px;background:var(--stamp)}
  .info-box{position:absolute;top:156px;height:111px;background:var(--navy-panel);border-radius:12px;padding:8px 10px}
  .info-box--offer{left:41px;width:152px}
  .info-box--included{left:201px;width:201px}
  .info-box__title{background:var(--sky-light);color:var(--white);font-weight:700;font-size:13px;text-align:center;border-radius:10px;padding:2px 0;margin-bottom:5px}
  .checklist{list-style:none}
  .checklist li{display:flex;align-items:center;gap:5px;color:var(--white);font-size:10.5px;font-weight:600;line-height:17px}
  .tick{width:9px;height:9px;flex:none}
  .story{position:absolute;left:41px;top:285px;width:372px;color:var(--white);font-size:9.6px;line-height:12.4px;font-weight:400}
  .reasons__title{position:absolute;left:41px;top:370px;color:var(--orange);font-size:11px;font-weight:700}
  .reasons{position:absolute;top:388px;list-style:none}
  .reasons--a{left:41px}
  .reasons--b{left:202px}
  .reasons li{display:flex;align-items:center;gap:5px;color:var(--white);font-size:9.8px;line-height:16.5px}
  .contact-pill{position:absolute;left:0;top:451px;width:351px;height:39px;background:var(--orange);border-radius:0 20px 20px 0;color:var(--white);font-weight:600;font-size:19px;line-height:39px;padding-left:39px;z-index:2}
  .contact-bar{position:absolute;left:0;top:478px;width:763px;height:67px;background:var(--sky);display:flex;align-items:center;padding:10px 0 0 44px;gap:12px;color:var(--white);font-weight:600;font-size:13px;white-space:nowrap}
  .contact-bar__item{display:flex;align-items:center;gap:5px}
  .contact-bar__sep{width:1.5px;height:18px;background:var(--white)}
  .icon{width:12px;height:12px;flex:none}
</style>
</head>
<body>

<!-- FRONT -->
<section class="card card--front" aria-label="Postcard front">
  <svg class="card__art" viewBox="0 0 763 545" aria-hidden="true">
    <defs>
      <linearGradient id="navyWash" x1="0" y1="0" x2="1" y2="1">
        <stop offset="0" stop-color="#1b3f7a"/><stop offset="1" stop-color="#0f2c5c"/>
      </linearGradient>
    </defs>
    <rect width="763" height="545" fill="url(#navyWash)"/>
    <path d="M0,150 C120,118 250,98 420,92 L420,545 L0,545 Z" fill="#fff"/>
    <path d="M262,170 C330,90 520,48 763,100" fill="none" stroke="var(--sky)" stroke-width="12"/>
    <path d="M0,545 L763,545 L763,470 C600,520 500,530 420,545 Z" fill="#2f7a68"/>
  </svg>
  <svg class="card__art" viewBox="0 0 763 545" role="img" aria-label="Photo: guests seated aboard a white pontoon boat cruising on green water">
    <defs>
      <linearGradient id="boatPhoto" x1="0" y1="0" x2="0.4" y2="1">
        <stop offset="0" stop-color="#d8dcd9"/><stop offset=".55" stop-color="#a9b1ad"/><stop offset="1" stop-color="#4f8c7c"/>
      </linearGradient>
    </defs>
    <path d="M300,545 C300,300 340,118 560,88 C680,74 763,110 763,125 L763,545 Z" fill="url(#boatPhoto)"/>
  </svg>
  <div class="brand brand--front"><span class="brand__dot"></span>Tidewell Charters</div>
  <h1 class="headline">PRIVATE<br>BOAT<br><span class="headline__accent">CHARTER</span><span class="headline__sub">for scattering ashes at sea</span></h1>
  <div class="tile tile--shells" role="img" aria-label="Photo: seashells on sand"></div>
  <div class="tile tile--dolphins" role="img" aria-label="Photo: dolphins leaping from the water"></div>
</section>

<!-- BACK -->
<section class="card card--back" aria-label="Postcard back">
  <svg class="card__art" viewBox="0 0 763 545" aria-hidden="true">
    <path d="M0,105 C120,150 300,145 380,90 C430,150 445,230 440,300 C435,380 405,430 360,478 L0,478 Z" fill="var(--navy)"/>
  </svg>
  <svg class="card__art" viewBox="0 0 763 545" role="img" aria-label="Photo: a motorboat with passengers on turquoise water">
    <defs>
      <linearGradient id="seaPhoto" x1="0" y1="0" x2="1" y2="1">
        <stop offset="0" stop-color="#9fd0c2"/><stop offset=".6" stop-color="#5fae98"/><stop offset="1" stop-color="#3d8a78"/>
      </linearGradient>
    </defs>
    <path d="M0,0 L430,0 C400,90 300,138 180,138 C100,138 40,124 0,105 Z" fill="url(#seaPhoto)"/>
  </svg>
  <div class="brand brand--back"><span class="brand__dot"></span>Tidewell Charters</div>
  <div class="stamp" aria-hidden="true"></div>

  <div class="info-box info-box--offer">
    <div class="info-box__title">What we offer:</div>
    <ul class="checklist">
      <li><svg class="tick" viewBox="0 0 10 10"><circle cx="5" cy="5" r="5" fill="#fff"/><path d="M2.6,5.2 L4.3,6.8 L7.4,3.6" fill="none" stroke="var(--navy-panel)" stroke-width="1.4"/></svg>Attended service,</li>
      <li><svg class="tick" viewBox="0 0 10 10"><circle cx="5" cy="5" r="5" fill="#fff"/><path d="M2.6,5.2 L4.3,6.8 L7.4,3.6" fill="none" stroke="var(--navy-panel)" stroke-width="1.4"/></svg>Unattended service,</li>
      <li><svg class="tick" viewBox="0 0 10 10"><circle cx="5" cy="5" r="5" fill="#fff"/><path d="M2.6,5.2 L4.3,6.8 L7.4,3.6" fill="none" stroke="var(--navy-panel)" stroke-width="1.4"/></svg>Memorial service,</li>
      <li><svg class="tick" viewBox="0 0 10 10"><circle cx="5" cy="5" r="5" fill="#fff"/><path d="M2.6,5.2 L4.3,6.8 L7.4,3.6" fill="none" stroke="var(--navy-panel)" stroke-width="1.4"/></svg>Anniversary service.</li>
    </ul>
  </div>
  <div class="info-box info-box--included">
    <div class="info-box__title">What's included:</div>
    <ul class="checklist">
      <li><svg class="tick" viewBox="0 0 10 10"><circle cx="5" cy="5" r="5" fill="#fff"/><path d="M2.6,5.2 L4.3,6.8 L7.4,3.6" fill="none" stroke="var(--navy-panel)" stroke-width="1.4"/></svg>Certificate of Ash Spreading,</li>
      <li><svg class="tick" viewBox="0 0 10 10"><circle cx="5" cy="5" r="5" fill="#fff"/><path d="M2.6,5.2 L4.3,6.8 L7.4,3.6" fill="none" stroke="var(--navy-panel)" stroke-width="1.4"/></svg>Onboard refreshments,</li>
      <li><svg class="tick" viewBox="0 0 10 10"><circle cx="5" cy="5" r="5" fill="#fff"/><path d="M2.6,5.2 L4.3,6.8 L7.4,3.6" fill="none" stroke="var(--navy-panel)" stroke-width="1.4"/></svg>Personalized music.</li>
    </ul>
  </div>

  <p class="story">People often choose to scatter ashes at sea because it symbolizes a deep connection to nature, representing a return to the elements and a sense of eternal continuity, particularly for those who loved the ocean or had a strong connection to maritime life; it can be a profound way to say goodbye and find peace in the vastness of the sea, often seen as a powerful symbol of the cycle of life and death.</p>

  <h2 class="reasons__title">Key reasons why people choose to scatter ashes at sea:</h2>
  <ul class="reasons reasons--a">
    <li><svg class="tick" viewBox="0 0 10 10"><circle cx="5" cy="5" r="5" fill="var(--sky-light)"/><path d="M2.6,5.2 L4.3,6.8 L7.4,3.6" fill="none" stroke="#fff" stroke-width="1.4"/></svg>Love for the Ocean:</li>
    <li><svg class="tick" viewBox="0 0 10 10"><circle cx="5" cy="5" r="5" fill="var(--sky-light)"/><path d="M2.6,5.2 L4.3,6.8 L7.4,3.6" fill="none" stroke="#fff" stroke-width="1.4"/></svg>Symbolic Meaning:</li>
    <li><svg class="tick" viewBox="0 0 10 10"><circle cx="5" cy="5" r="5" fill="var(--sky-light)"/><path d="M2.6,5.2 L4.3,6.8 L7.4,3.6" fill="none" stroke="#fff" stroke-width="1.4"/></svg>Connection to Nature:</li>
  </ul>
  <ul class="reasons reasons--b">
    <li><svg class="tick" viewBox="0 0 10 10"><circle cx="5" cy="5" r="5" fill="var(--sky-light)"/><path d="M2.6,5.2 L4.3,6.8 L7.4,3.6" fill="none" stroke="#fff" stroke-width="1.4"/></svg>Sense of Release:</li>
    <li><svg class="tick" viewBox="0 0 10 10"><circle cx="5" cy="5" r="5" fill="var(--sky-light)"/><path d="M2.6,5.2 L4.3,6.8 L7.4,3.6" fill="none" stroke="#fff" stroke-width="1.4"/></svg>Spiritual Beliefs:</li>
  </ul>

  <div class="contact-pill">Our contact information:</div>
  <div class="contact-bar">
    <span class="contact-bar__item"><svg class="icon" viewBox="0 0 12 12"><circle cx="6" cy="6" r="5.3" fill="none" stroke="#fff" stroke-width="1.2"/><path d="M0.8,6 H11.2 M6,0.8 C3.5,3.5 3.5,8.5 6,11.2 M6,0.8 C8.5,3.5 8.5,8.5 6,11.2" fill="none" stroke="#fff" stroke-width="1"/></svg>www.tidewellcharters.example</span>
    <span class="contact-bar__sep"></span>
    <span class="contact-bar__item"><svg class="icon" viewBox="0 0 12 12"><circle cx="6" cy="6" r="6" fill="#fff"/><path d="M4,3 L5,4.6 L4.4,5.3 C4.9,6.4 5.6,7.1 6.7,7.6 L7.4,7 L9,8 L8.5,9 C6,9 3,6 3,3.5 Z" fill="var(--sky)"/></svg>(727) 555-0148</span>
    <span class="contact-bar__sep"></span>
    <span class="contact-bar__item"><svg class="icon" viewBox="0 0 12 12"><path d="M6,0.6 C3.6,0.6 2,2.3 2,4.5 C2,7.4 6,11.6 6,11.6 C6,11.6 10,7.4 10,4.5 C10,2.3 8.4,0.6 6,0.6 Z" fill="#fff"/><circle cx="6" cy="4.5" r="1.5" fill="var(--sky)"/></svg>452 Marlowe St., Clearwater, FL 33755,</span>
  </div>
</section>

</body>
</html>
```